Design 2015 Winter themed holiday card

We need a holiday card for our company.

The attached brief provides all the information for the design. We provided two images for the cover or if you have something better.

CARD DESIGN 4" x 6" Vertical Folded Card
Bleed: The extra .0625" on each side of your artwork that bleeds off the edge of the piece and ensures your piece will not end up with white borders.
Trim: The final size the printed piece will be.
Safe: The .0625" area from the final trim size. Do not place text or important imagery beyond the safe line to avoid it getting cut off when the finished piece is trimmed to final size.
Corner Rounding, where available, can be 1/8" or 5/16". Examples are provided in the image below.
1/8" is a "tighter" or "smaller" corner radius.
5/16" is a "wider" or "larger" corner radius.

Target Market(s)

Government agencies, businesses and nonprofits

Industry/Entity Type

It Company

Font styles to use
Serif
Sans Serif

Requirements
Must have
• Please follow the design brief: QKRP-Strategy-Brief-Holiday-Card-11042015.pdf
• It includes the fonts, colors, design parameters - please review it before designing. I've included two previous holiday cards for your review.
• Please add "Seasons Greetings" on the cover.

```html
<!DOCTYPE html>
<html lang="en">
<head>
<meta charset="utf-8">
<title>Holiday Card – Inside Spread</title>
<link rel="stylesheet" href="https://fonts.googleapis.com/css2?family=Sofia&family=Caveat+Brush&family=Kaushan+Script&family=Courgette&family=Handlee&family=Mrs+Saint+Delafield&family=Yellowtail&family=Dancing+Script:wght@500&family=Josefin+Slab:wght@600&display=swap">
<style>
  :root {
    --paper: #ffffff;
    --ink: #111111;
    --trim-line: #e6a3d8;
    --fold-line: #a9a9a9;
  }
  html, body {
    margin: 0;
    padding: 0;
    overflow: hidden;
    background: var(--paper);
  }
  .card-spread {
    position: relative;
    width: 1200px;
    height: 911px;
    background: var(--paper);
    color: var(--ink);
    overflow: hidden;
  }
  .guides {
    position: absolute;
    inset: 0;
  }
  .signature {
    position: absolute;
    left: 308px;
    transform: translate(-50%, -50%);
    margin: 0;
    white-space: nowrap;
    line-height: 1;
  }
  .sig-1 { top: 174px; font-family: "Sofia", cursive; font-size: 46px; }
  .sig-2 { top: 246px; font-family: "Caveat Brush", cursive; font-size: 52px; letter-spacing: 1px; }
  .sig-3 { top: 322px; font-family: "Kaushan Script", cursive; font-size: 46px; }
  .sig-4 { top: 392px; font-family: "Courgette", cursive; font-size: 44px; font-style: italic; }
  .sig-5 { top: 467px; font-family: "Handlee", cursive; font-size: 42px; }
  .sig-6 { top: 549px; font-family: "Mrs Saint Delafield", cursive; font-size: 50px; }
  .sig-7 { top: 615px; font-family: "Yellowtail", cursive; font-size: 52px; }
  .sig-8 { top: 690px; font-family: "Dancing Script", cursive; font-size: 50px; font-weight: 500; }

  .message, .closing {
    position: absolute;
    margin: 0;
    font-family: "Josefin Slab", serif;
    font-weight: 600;
    font-size: 20px;
    line-height: 31px;
  }
  .message { left: 685px; top: 282px; }
  .closing { right: 80px; top: 528px; text-align: right; }
</style>
</head>
<body>
  <main class="card-spread">
    <svg class="guides" width="1200" height="911" viewBox="0 0 1200 911" aria-hidden="true">
      <line x1="0" y1="1" x2="1200" y2="1" stroke="var(--fold-line)" stroke-width="1.5"/>
      <line x1="0" y1="907" x2="1200" y2="907" stroke="var(--fold-line)" stroke-width="1.5"/>
      <rect x="6" y="6" width="1188" height="896" rx="16" fill="none" stroke="var(--trim-line)" stroke-width="1.5"/>
      <line x1="599" y1="0" x2="599" y2="911" stroke="var(--fold-line)" stroke-width="1.5"/>
    </svg>

    <section class="signatures" aria-label="Team signatures">
      <p class="signature sig-1">Owen Marsh</p>
      <p class="signature sig-2">Dario Velente</p>
      <p class="signature sig-3">Marla Penwick</p>
      <p class="signature sig-4">Ilse Verhoven</p>
      <p class="signature sig-5">Nora Feldan</p>
      <p class="signature sig-6">Greta Lindquist</p>
      <p class="signature sig-7">Sonia Carver</p>
      <p class="signature sig-8">Martin Holloway</p>
    </section>

    <p class="message">
      As this year draws to a close, we are grateful for<br>
      the opportunities we have had to work together.<br>
      We wish you all the best for the year to come.
    </p>

    <p class="closing">
      Happy Holidays from the<br>
      Quill Kettle River Partners team
    </p>
  </main>
</body>
</html>
```